White Paper and One-Page Advertisement for TELVAMORE-QX

I need both documents to be better formatted and designed so they look professional, not something someone with mediocre word skills put together. They will go out to 1000s of industry professionals, and they need to look sharp. I need them to have my company's color palate logo, and branding on it similar to how it is now, but better. Please do not change any of the written content, but it can be arranged in any other format you think is better. Smart art and things i've already used can be omitted in favor of better designs. The developer is free to use their creativity. White paper should not be longer than the three pages unless necessary.

Target Market(s)

Life Sciences supply chain professionals

Colors
33b8a4
0592cd
9bcb3c
fbee3e
3277b5

Requirements
Must have
• Must be professional looking and not look like something done in word. Please use the color palate as seen on the documents.
Should not have
• Any changes to the written content.

```html
<!DOCTYPE html>
<html lang="en">
<head>
<meta charset="utf-8">
<title>TELVAMORE-QX White Paper – Changing Pharma's Paradigm of Waste</title>
<link rel="stylesheet" href="https://fonts.googleapis.com/css2?family=Oswald:wght@500;600&family=Lato:wght@400;700;900&display=swap">
<style>
:root{
  --stage:#4b3d69;
  --paper:#ffffff;
  --paper-grey:#ececec;
  --orange:#d98a1f;
  --orange-dark:#c0761a;
  --teal:#3d8a8b;
  --teal-dark:#2f7172;
  --ink:#1d1d1d;
  --muted:#444;
  --green:#9bcb3c;
  --photo-a:#6d5a4e;
  --photo-b:#b9b2a8;
  --photo-c:#8fa7c2;
}
*{box-sizing:border-box;margin:0;padding:0}
html,body{width:1200px;height:3191px;overflow:hidden;background:var(--stage)}
body{position:relative;font-family:"Lato",Arial,sans-serif;color:var(--ink)}
.page{position:absolute;background:var(--paper);overflow:hidden;box-shadow:0 10px 30px rgba(0,0,0,.35)}
.page-frame{position:absolute;inset:0}
.abs{position:absolute}

/* ---------- cover ---------- */
.cover{left:220px;top:60px;width:760px;height:1075px}
.brand{position:absolute;right:40px;top:88px;display:flex;align-items:center;gap:10px}
.brand-dot{width:26px;height:26px;border-radius:50%;background:var(--green)}
.brand-name{font-family:"Lato",Arial,sans-serif;font-weight:900;font-size:24px;color:var(--teal-dark);letter-spacing:.5px}
.title-band{left:60px;top:300px;width:680px;height:60px;background:var(--teal);color:#fff;
  font-family:"Oswald",Arial,sans-serif;font-weight:600;font-size:38px;line-height:60px;text-align:center;letter-spacing:.5px}
.photo-frame{left:80px;top:368px;width:640px;height:190px;background:#fff;border:1px solid #d5d5d5;display:flex;gap:8px;padding:8px}
.photo{flex:1}
.photo-a{background:linear-gradient(160deg,var(--photo-a),#3b302b)}
.photo-b{background:linear-gradient(160deg,#d4cec6,var(--photo-b))}
.photo-c{background:linear-gradient(160deg,#c9d6e4,var(--photo-c))}
.subtitle-band{left:60px;top:562px;width:680px;height:80px;background:var(--teal);color:#fff;
  font-family:"Lato",Arial,sans-serif;font-weight:700;font-size:22px;line-height:26px;text-align:center;padding-top:14px}
.byline{left:60px;top:646px;width:640px;text-align:right;font-weight:900;font-size:22px}
.section-tab{background:var(--orange);color:#fff;font-family:"Oswald",Arial,sans-serif;font-weight:500;
  clip-path:polygon(0 0,92% 0,100% 100%,0 100%)}
.cover .section-tab{left:60px;top:690px;width:240px;height:32px;font-size:22px;line-height:32px;padding-left:14px}
.cover-body{left:70px;top:732px;width:650px;font-size:14.5px;line-height:20px;font-weight:700;text-align:justify}

/* ---------- inner page ---------- */
.inner{left:220px;top:1195px;width:760px;height:1075px}
.col{position:absolute;font-size:12.5px;line-height:17px;color:var(--muted)}
.col p{margin-bottom:10px;text-align:justify}
.col h3{font-family:"Oswald",Arial,sans-serif;font-weight:500;font-size:15px;color:var(--teal-dark);margin:4px 0 6px}
.col ul{list-style:none;margin-bottom:10px}
.col li{padding-left:14px;position:relative;margin-bottom:3px}
.col li::before{content:"";position:absolute;left:2px;top:6px;width:6px;height:6px;background:var(--orange)}
.inner .section-tab{height:28px;font-size:18px;line-height:28px;padding-left:12px}

/* ---------- spread ---------- */
.spread-left{left:60px;top:2350px;width:540px;height:764px}
.spread-right{left:600px;top:2350px;width:540px;height:764px}
.spread .col{font-size:9px;line-height:12.5px}
.spread .col p{margin-bottom:7px}
.spread .col h3{font-size:11px;margin:2px 0 4px}
.spread .section-tab{height:20px;font-size:12px;line-height:20px;padding-left:8px}
.spread-photo{background:linear-gradient(150deg,#7d6a55,#3f4a55)}
.gutter{position:absolute;left:598px;top:2350px;width:4px;height:764px;background:linear-gradient(90deg,rgba(0,0,0,.25),rgba(0,0,0,0))}
</style>
</head>
<body>

<!-- Cover page -->
<section class="page cover" aria-label="White paper cover">
  <svg class="page-frame" width="760" height="1075" viewBox="0 0 760 1075" aria-hidden="true">
    <rect width="760" height="1075" fill="#ffffff"/>
    <polygon points="0,0 760,0 760,260 0,260" fill="var(--orange)"/>
    <polygon points="150,0 760,0 760,205 190,205" fill="var(--paper-grey)"/>
    <rect x="0" y="260" width="60" height="815" fill="var(--orange)"/>
    <rect x="60" y="260" width="700" height="700" fill="#ffffff"/>
    <rect x="0" y="960" width="760" height="30" fill="var(--orange)"/>
    <rect x="0" y="990" width="760" height="85" fill="var(--teal)"/>
  </svg>
  <div class="brand"><span class="brand-dot"></span><span class="brand-name">TELVAMORE-QX</span></div>
  <h1 class="abs title-band">CHANGING PHARMA'S PARADIGM OF WASTE</h1>
  <div class="abs photo-frame">
    <div class="photo photo-a" role="img" aria-label="Photo of a young woman"></div>
    <div class="photo photo-b" role="img" aria-label="Photo of a baby"></div>
    <div class="photo photo-c" role="img" aria-label="Photo of an elderly woman"></div>
  </div>
  <h2 class="abs subtitle-band">How Pharma's Demand Volatility Could Be Costing<br>You Millions in Material Write-downs &amp; Procurement</h2>
  <p class="abs byline">Dana Holloway &nbsp;|&nbsp; August</p>
  <h3 class="abs section-tab">Overview</h3>
  <p class="abs cover-body">Demand volatility is a challenge for very supply chain. It strikes at the end of supply chain causing a "bullwhip effect" that becomes exponentially more impactful further back in the chain. For Pharma, the effect is strongest in manufacturing and procurement, specifically with raw materials and consumables. Swings in demand can cripple lean supply chains, cause stock outs, inflate material prices, make lean planning ineffective, and cause significant write-downs due to obsolete materials; ultimately inflating CoGS and reducing net income. These swings can also cause inventory costs to inflate, materials to expire or become obsolete, higher disposal fees, and a larger carbon footprint. The yearly financial impacts are staggering considering Pharma's economic footprint. Twenty of Pharma's top 100 companies were sampled using 2015 &amp; 2016 financial figures1-2-3-4. Industry estimates for waste include:</p>
</section>

<!-- Inner page -->
<section class="page inner" aria-label="White paper page two">
  <svg class="page-frame" width="760" height="1075" viewBox="0 0 760 1075" aria-hidden="true">
    <rect width="760" height="1075" fill="#ffffff"/>
    <rect x="0" y="0" width="60" height="1075" fill="var(--orange)"/>
    <rect x="60" y="0" width="700" height="24" fill="var(--paper-grey)"/>
    <rect x="0" y="990" width="760" height="30" fill="var(--orange)"/>
    <rect x="0" y="1020" width="760" height="55" fill="var(--teal)"/>
  </svg>
  <div class="col" style="left:85px;top:50px;width:300px">
    <h3 class="section-tab" style="color:#fff;width:220px">Industry Estimates</h3>
    <ul>
      <li>Material write-downs: an average of 2–4% of yearly CoGS</li>
      <li>Inventory carrying costs: 20–30% of inventory value</li>
      <li>Disposal fees for expired and obsolete stock</li>
      <li>Excess safety stock held against swings in demand</li>
    </ul>
    <p>Across the twenty companies sampled, these losses add up to hundreds of millions of dollars each year, most of it in high-quality materials that are still fit for use by another organization.</p>
    <h3>Why It Persists</h3>
    <p>Forecasts change faster than supply contracts, minimum order quantities and shelf lives allow. Materials bought for one program are stranded when plans shift, and the cheapest path is often a write-off followed by disposal.</p>
    <p>Few tools exist that let companies share surplus with like-minded life sciences organizations, so value leaves the industry as waste.</p>
  </div>
  <div class="col" style="left:410px;top:50px;width:320px">
    <h3 class="section-tab" style="color:#fff;width:220px">Baseline Problem</h3>
    <p><strong>What:</strong></p>
    <ul>
      <li>Disposal of high-quality materials, equipment, spare parts</li>
      <li>Single or limited sources of supply</li>
      <li>Inability to collaborate with like-minded life sciences companies</li>
      <li>Write-downs due to materials write-downs</li>
      <li>Inventory carrying costs</li>
      <li>Business continuity risk</li>
      <li>Disposal costs</li>
      <li>Environmental footprint</li>
      <li>Loss of materials</li>
    </ul>
    <p><strong>Who:</strong> Pharma, Related Industries, Procurement, Quality, Supply Chain, and Finance</p>
    <p><strong>When:</strong> Commercial &amp; clinical production, R&amp;D, sourcing, production planning, quality testing</p>
    <p><strong>Why:</strong> Transitional periods, e.g., product intro growth, decline, seasonality, economic uncertainty, and unforeseen events</p>
    <p><strong>How do we know it's there?</strong> We know where it is taking place, and it's in our data.</p>
    <h3>Bottom Line Impact</h3>
    <ul>
      <li>Write-downs/offs and 3rd party disposal costs</li>
      <li>Lost value of materials &amp; supplier expertise</li>
      <li>Amplified bullwhip effect</li>
      <li>Contribution to global warming through incineration, inactivation, and landfill</li>
      <li>Strain on ISO 14000 &amp; 9000 programs</li>
      <li>High environment and compliance burden</li>
      <li>Weaker procurement and supply chain operations</li>
    </ul>
  </div>
</section>

<!-- Two-page spread -->
<section class="page spread spread-left" aria-label="White paper spread, left page">
  <svg class="page-frame" width="540" height="764" viewBox="0 0 540 764" aria-hidden="true">
    <rect width="540" height="764" fill="#ffffff"/>
    <rect x="0" y="0" width="42" height="764" fill="var(--orange)"/>
    <rect x="0" y="704" width="540" height="20" fill="var(--orange)"/>
    <rect x="0" y="724" width="540" height="40" fill="var(--teal)"/>
  </svg>
  <div class="col" style="left:60px;top:28px;width:210px">
    <h3 class="section-tab" style="color:#fff;width:170px">The Cost of Doing Nothing</h3>
    <p>Every year, usable materials are destroyed because the systems that plan, buy and store them cannot adapt to sudden swings in demand. The costs land on the income statement and on the environment.</p>
    <p>Write-downs reduce net income, disposal fees grow with volume, and each incinerated lot adds to the carbon footprint that companies have pledged to shrink.</p>
    <h3>Where Waste Begins</h3>
    <ul>
      <li>Forecast changes late in the cycle</li>
      <li>Minimum order quantities</li>
      <li>Short shelf lives</li>
      <li>Program cancellations</li>
    </ul>
    <p>Each of these turns good stock into surplus that no one inside the company can use.</p>
  </div>
  <div class="col" style="left:290px;top:28px;width:220px">
    <h3 class="section-tab" style="color:#fff;width:170px">Overview</h3>
    <p>Supply chain leaders already measure this loss, yet few have a channel to recover value from it. Surplus is written off quietly and sent for disposal.</p>
    <p>A shared exchange between life sciences companies would let qualified materials move to those who need them, reducing cost for both sides.</p>
    <h3>Key Figures</h3>
    <ul>
      <li>20 of the top 100 companies sampled</li>
      <li>2015 &amp; 2016 financial figures</li>
      <li>Write-downs reported as part of CoGS</li>
    </ul>
    <p>The findings show that waste is not an exception but a recurring line item across the industry.</p>
  </div>
</section>
<div class="gutter" aria-hidden="true"></div>
<section class="page spread spread-right" aria-label="White paper spread, right page">
  <svg class="page-frame" width="540" height="764" viewBox="0 0 540 764" aria-hidden="true">
    <rect width="540" height="764" fill="#ffffff"/>
    <rect x="498" y="0" width="42" height="764" fill="var(--orange)"/>
    <rect x="0" y="704" width="540" height="20" fill="var(--orange)"/>
    <rect x="0" y="724" width="540" height="40" fill="var(--teal)"/>
  </svg>
  <div class="col" style="left:28px;top:28px;width:215px">
    <h3 class="section-tab" style="color:#fff;width:170px">Methodology &amp; Assumptions</h3>
    <p>Company reports were reviewed for inventory write-downs, disposal and carrying costs. Figures were grouped by size and segment to build an industry estimate.</p>
    <p>Where firms did not report a value, a conservative range drawn from peers was applied.</p>
    <h3>Limitations</h3>
    <p>Reported write-downs rarely separate materials from finished goods, so the true scale of material waste is likely higher than shown.</p>
    <ul>
      <li>Public filings only</li>
      <li>Two fiscal years</li>
      <li>Currency shown in USD</li>
    </ul>
  </div>
  <div class="col" style="left:262px;top:28px;width:220px">
    <h3 class="section-tab" style="color:#fff;width:170px">Baseline Problem</h3>
    <p>Demand volatility forces teams to hold extra stock, pay rush premiums and accept losses when plans change.</p>
    <ul>
      <li>Disposal of quality materials</li>
      <li>Limited sources of supply</li>
      <li>Inventory carrying costs</li>
      <li>Business continuity risk</li>
      <li>Environmental footprint</li>
    </ul>
    <p>These costs are shared by procurement, quality, supply chain and finance alike.</p>
  </div>
  <div class="abs spread-photo" style="left:262px;top:520px;width:220px;height:160px" role="img" aria-label="Photo of a pharmaceutical production team at work"></div>
</section>

</body>
</html>
```